RVQ Corporate Identity

As the first stage of implementing a new corporate identity we need a logo, letterhead and business card design.

The Residents Alliance Federation of Tasgrove Inc (RVQ) is a non-profit, volunteer-run association representing owners of strata-titled residential developments. We provide education, information and lobbying to improve the management of apartment complexes and the lives of those living in them. We’re all about “owners helping owners”. More information on our organisation can be seen at www.rvq-example.org.au.

The logo will be used on our own stationery and promotional materials. It will also be provided to our sponsors for use on their collateral – as such it needs to be of a ‘standard’ size so it can be easily used in a wide of materials.

Once we have chosen the new logo and corresponding design concept we will open a new contest for a complementary layout design for our website.
Updates

Thank you to everyone who submitted designs for us. There were many really great concepts, and we appreciate the effort that everyone went to - but as you know we can only choose one.

Kind regards
Margaret

Target Market(s)

The primary audience is Owners of residential apartments - both resident owners and investor owners.

Secondary audiences – current and potential sponsors; organisations providing products & services to Owners Corporations & Body Corporates

Industry/Entity Type

Non-Profit

Requirements
Must have
• The design and colours should reflect a sense of community, coupled with authority, professionalism and knowledge.

We are open to all ideas.

```html
<!DOCTYPE html>
<html lang="en">
<head>
<meta charset="utf-8">
<title>RVQ Stationery</title>
<link rel="stylesheet" href="https://fonts.googleapis.com/css2?family=Questrial&display=swap">
<style>
  :root {
    --bg: #ffffff;
    --paper: #f6f6f6;
    --edge: #e2e2e2;
    --ink: #8a8a8a;
    --teal: #1b9bd1;
    --green: #b5c61a;
    --orange: #ee8a0c;
  }
  * { margin: 0; padding: 0; box-sizing: border-box; }
  html, body { width: 1200px; height: 1200px; overflow: hidden; background: var(--bg); }
  body { position: relative; font-family: "Questrial", sans-serif; color: var(--ink); }

  .letterhead {
    position: absolute; left: 264px; top: 150px; width: 636px; height: 900px;
    background: var(--paper); border: 1px solid var(--edge); overflow: hidden;
  }
  .wordmark { display: flex; align-items: center; gap: 8px; color: var(--teal); font-weight: 400; letter-spacing: 1px; white-space: nowrap; }
  .wordmark-dot { width: 14px; height: 14px; border-radius: 50%; background: var(--orange); }
  .letterhead .wordmark { position: absolute; left: 36px; top: 38px; font-size: 56px; line-height: 1; }
  .letterhead .wordmark-dot { width: 18px; height: 18px; }
  .sender { position: absolute; left: 38px; top: 118px; font-size: 9.5px; line-height: 1.45; }
  .sender p + p { margin-top: 10px; }
  .letter-footer { position: absolute; left: 38px; right: 150px; bottom: 26px; font-size: 6.5px; line-height: 1.5; }
  .footer-band { position: absolute; right: 0; bottom: 0; width: 120px; height: 12px; background: var(--green); }

  .card {
    position: absolute; width: 166px; height: 106px; background: var(--paper);
    border: 1px solid var(--edge); border-radius: 5px; overflow: hidden;
  }
  .card .wordmark { position: absolute; left: 12px; top: 12px; font-size: 26px; line-height: 1; }
  .card .wordmark-dot { width: 9px; height: 9px; }
  .card-details { position: absolute; left: 12px; top: 48px; display: flex; gap: 8px; font-size: 5px; line-height: 1.45; white-space: nowrap; }
  .card-details .person { text-align: right; }
  .card-back { background: var(--green); border-color: var(--green); display: flex; align-items: center; justify-content: center; }
  .card-back .wordmark { position: static; color: var(--bg); font-size: 34px; }
  .card-back .wordmark-dot { background: var(--bg); width: 11px; height: 11px; }
  .card-a { left: 832px; top: 522px; }
  .card-b { left: 648px; top: 588px; }
  .card-c { left: 832px; top: 652px; }
</style>
</head>
<body>
  <section class="letterhead">
    <div class="wordmark"><span>RVQ</span><span class="wordmark-dot"></span></div>
    <div class="sender">
      <p>PO Box 4821<br>Harbour Arcade Building<br>TSG 7420</p>
      <p>M 0400 555 019<br>E. office@rvq-example.org.au</p>
    </div>
    <p class="letter-footer">The Residents Alliance Federation of Tasgrove Inc is a voluntary association made up of members of the public, including strata owners and committee members. Registered under the Associations Act 2011.</p>
    <div class="footer-band"></div>
  </section>

  <article class="card card-a">
    <div class="wordmark"><span>RVQ</span><span class="wordmark-dot"></span></div>
    <div class="card-details">
      <p class="person">Daniel Wren<br>Committee Secretary</p>
      <p>PO Box 4821<br>Harbour Arcade Building<br>TSG 7420<br><br>M 0400 555 019<br>E office@rvq-example.org.au</p>
    </div>
  </article>

  <article class="card card-b">
    <div class="wordmark"><span>RVQ</span><span class="wordmark-dot"></span></div>
    <div class="card-details">
      <p class="person">Margaret Hale<br>Executive Officer</p>
      <p>PO Box 4821<br>Harbour Arcade Building<br>TSG 7420<br><br>M 0400 555 019<br>E margaret@rvq-example.org.au</p>
    </div>
  </article>

  <article class="card card-back card-c">
    <div class="wordmark"><span>RVQ</span><span class="wordmark-dot"></span></div>
  </article>
</body>
</html>
```